Premium Food Label Design – High-End Boutique Jar Labels (3 Sizes)

I require a complete jar label redesign across three sizes:
75mm x 130mm (Large & Medium)
55mm x 120mm (Small)
45mm x 120mm (XS)

The design must feel professional, modern, elegant, and high-end boutique.
Primary aesthetic: white, minimal, refined, with accents in soft brown and gold/bronze. (see prefer colours of logo in OLD LABEL PDF)
Transparent background required.

I have attached my current label for wording reference only — I want to move away from the kraft look entirely.
The label must include all existing details, plus a dedicated space to manually add batch number and date.

IMPORTANT: Final files must be supplied as editable Adobe Illustrator (.AI) files with live text layers (not outlined) so I can update them as needed.
Logo is attached. I’m open to a fresh, elevated design direction aligned with a premium brand feel.
Updates

Low design quality

Target Market(s)

People who appreciate high-end, thoughtfully crafted food and are willing to pay for quality

Industry/Entity Type

Gourmet Food / Artisan Food Packaging

Requirements
Must have
• Premium, minimal aesthetic, Strong typography hierarchy, White background, Consistency across 3 sizes
Nice to have
• Elevated “Velvet Orchard” styling
Should not have
• No bright or bold colours, No clutter or overcrowding, No heavy borders or thick frames,No “homemade/craft” fonts

```html
<!DOCTYPE html>
<html lang="en">
<head>
<meta charset="utf-8">
<title>Tomato Relish – Jar Label</title>
<link rel="stylesheet" href="https://fonts.googleapis.com/css2?family=Fredoka:wght@600&family=Quicksand:wght@400;500;700&family=Gochi+Hand&display=swap">
<style>
  :root {
    --bg: #ececec;
    --paper: #ffffff;
    --cocoa: #45220f;
    --ink: #3a2112;
    --line: #4a2a18;
  }
  * { margin: 0; padding: 0; box-sizing: border-box; }
  html, body { width: 1200px; height: 1200px; overflow: hidden; background: var(--bg); }
  .canvas { position: relative; width: 1200px; height: 1200px; }

  .label {
    position: absolute; top: 150px; width: 522px; height: 900px;
    background: var(--paper);
  }
  .label--front { left: 62px; }
  .label--back  { left: 618px; }

  .front-frame { position: absolute; inset: 0; }

  .title-band {
    position: absolute; left: 0; top: 112px; width: 100%; height: 248px;
    background: var(--cocoa);
    display: flex; flex-direction: column; align-items: center; justify-content: center;
    color: var(--paper);
    font-family: "Fredoka", sans-serif; font-weight: 600;
    font-size: 104px; line-height: 108px; letter-spacing: 1px;
  }

  .brand {
    position: absolute; left: 0; top: 470px; width: 100%;
    text-align: center; color: var(--ink);
    font-family: "Quicksand", sans-serif; font-weight: 400;
  }
  .brand__main { display: block; font-size: 74px; line-height: 84px; letter-spacing: 6px; }
  .brand__sub  { display: block; font-size: 42px; line-height: 52px; letter-spacing: 5px; }

  .tagline {
    position: absolute; left: 0; top: 640px; width: 100%; text-align: center;
    font-family: "Gochi Hand", cursive; font-size: 38px; color: #1f1410;
  }
  .net-weight {
    position: absolute; left: 0; top: 762px; width: 100%; text-align: center;
    font-family: "Gochi Hand", cursive; font-size: 32px; color: #1f1410;
  }

  .back-copy {
    position: absolute; left: 27px; width: 380px;
    font-family: "Quicksand", sans-serif; font-weight: 500;
    font-size: 21px; line-height: 26.5px; color: var(--ink);
  }
  .intention   { top: 38px; }
  .ingredients { top: 378px; }
  .storage     { top: 509px; font-weight: 700; text-transform: uppercase; }
  .batch       { top: 668px; font-weight: 700; }
  .maker       { top: 748px; }
</style>
</head>
<body>
<main class="canvas">

  <section class="label label--front">
    <svg class="front-frame" width="522" height="900" viewBox="0 0 522 900" aria-hidden="true">
      <path d="M35 34 H488 V575 A226.5 290 0 0 1 35 575 Z" fill="none" stroke="var(--line)" stroke-width="1.6"/>
    </svg>
    <h1 class="title-band"><span>Tomato</span><span>Relish</span></h1>
    <p class="brand">
      <span class="brand__main">HEARTH &amp;</span>
      <span class="brand__sub">THYME</span>
    </p>
    <p class="tagline">Made with love</p>
    <p class="net-weight">375g</p>
  </section>

  <section class="label label--back">
    <p class="back-copy intention">Velvet Orchard<br>What is made with love is felt<br>in return.<br>May this relish nourish more<br>than the meal- bringing<br>comfort, connection, and joy<br>to every moment shared.</p>
    <p class="back-copy ingredients">Ingredients: Tomatoes, onion,<br>sugar, vinegar, salt, spices,<br>thickener<br>(cornflour)</p>
    <p class="back-copy storage">Storage: keep refrigerated<br>once opened</p>
    <p class="back-copy batch">Batch #....................<br>Date:....................</p>
    <p class="back-copy maker">Made by Hearth &amp; Thyme, QLD,<br>Australia<br>W: hearthandthyme.com<br>E: info@hearthandthyme.com</p>
  </section>

</main>
</body>
</html>
```